Sports Field sign

Our business provides audio visual solutions to corporate and government clients. We have purchased space at a sports field to place two signs to promote our business. We need to provide the artwork in high res format for a sign to be placed at a sports oval. The physical sign will be 900mm high and 7000mm long. It needs to include our logo, contact number, and the services we offer. It needs to be tidy, easy to read and easily visible from a distance. The sample I have done is very basic but covers what we need - I would expect that a designer can produce an eye-catching impressive sign with this much space to work with., and may even include some flashy background, an image or creative design to get attention.

examples of what signs are up at the oval now here - https://twitter.com/KPQ/status/1742906318845210937?s=20&t=9-bHRm4kwqZuLEO7_f_NxZ

Our Company web site is www.brightlinkav.com.au

```html
<!DOCTYPE html>
<html lang="en">
<head>
<meta charset="utf-8">
<title>brightlink av – Sports Field Sign</title>
<link href="https://fonts.googleapis.com/css2?family=Arimo:wght@400;700&family=Archivo+Black&display=swap" rel="stylesheet">
<style>
  :root {
    --navy: #1b3260;
    --blue: #2d5ba8;
    --sky: #6a9fd6;
    --white: #ffffff;
  }
  * { margin: 0; padding: 0; box-sizing: border-box; }
  html, body { width: 1199px; height: 1200px; overflow: hidden; }
  body { position: relative; background: var(--white); font-family: "Arimo", Arial, sans-serif; }

  .stage-light { position: absolute; left: 0; top: 0; width: 1199px; height: 593px; background: var(--white); }
  .stage-dark { position: absolute; left: 0; top: 593px; width: 1199px; height: 607px; background: var(--navy); }

  .sign {
    position: absolute; left: 70px; width: 1058px; height: 176px; overflow: hidden;
  }
  .sign--dark { top: 212px; background: var(--navy); --ink: var(--white); --url: var(--white); }
  .sign--light { top: 780px; background: var(--white); --ink: var(--navy); --url: var(--navy); }

  .brand {
    position: absolute; left: 16px; top: 0; width: 200px; height: 176px;
    display: flex; align-items: center; gap: 10px;
  }
  .brand__mark { width: 22px; height: 22px; background: var(--sky); flex: none; }
  .brand__name { font-size: 25px; font-weight: 400; color: var(--ink); letter-spacing: -0.3px; white-space: nowrap; }

  .services { position: absolute; left: 243px; top: 20px; list-style: none; }
  .services li {
    position: relative; padding-left: 18px; height: 35px; line-height: 30px;
    font-size: 25px; font-weight: 700; color: var(--ink); letter-spacing: 0.4px; white-space: nowrap;
  }
  .services li::before {
    content: ""; position: absolute; left: 0; top: 12px; width: 7px; height: 7px; border-radius: 50%; background: var(--ink);
  }

  .contact-panel { position: absolute; left: 586px; top: 0; width: 472px; height: 176px; }
  .contact-panel__backdrop {
    position: absolute; inset: 0;
    background: linear-gradient(90deg, var(--blue) 0%, var(--sky) 45%, var(--sky) 55%, var(--blue) 100%);
  }
  .phone {
    position: absolute; left: 8px; top: 36px; width: 460px; text-align: center;
    font-family: "Archivo Black", "Arial Black", sans-serif; font-size: 62px; line-height: 62px;
    color: var(--white); letter-spacing: 0.5px; white-space: nowrap;
  }
  .tagline {
    position: absolute; left: 9px; top: 96px; width: 458px; height: 19px; background: var(--white);
    display: flex; justify-content: space-between; align-items: center; padding: 0 5px;
    font-size: 14px; font-weight: 700; color: var(--navy); letter-spacing: 0.3px;
  }
  .website {
    position: absolute; right: 4px; top: 150px;
    font-size: 18px; font-weight: 700; color: var(--url); letter-spacing: 0.3px;
  }
</style>
</head>
<body>
  <div class="stage-light"></div>
  <div class="stage-dark"></div>

  <section class="sign sign--dark">
    <div class="brand"><span class="brand__mark"></span><span class="brand__name">brightlink av</span></div>
    <ul class="services">
      <li>VIDEO CONVERENCING</li>
      <li>DIGITAL SIGNAGE</li>
      <li>L.E.D VIDEO WALLS</li>
      <li>AUDIO SOLUTIONS</li>
    </ul>
    <div class="contact-panel">
      <div class="contact-panel__backdrop" role="img" aria-label="Blue geometric backdrop behind contact details"></div>
      <div class="phone">1300 555 019</div>
      <div class="tagline"><span>DESIGN</span><span>–</span><span>CONSULTING</span><span>–</span><span>SERVICE</span><span>–</span><span>MAINTENANCE</span></div>
      <div class="website">www.brightlinkav.com.au</div>
    </div>
  </section>

  <section class="sign sign--light">
    <div class="brand"><span class="brand__mark"></span><span class="brand__name">brightlink av</span></div>
    <ul class="services">
      <li>VIDEO CONVERENCING</li>
      <li>DIGITAL SIGNAGE</li>
      <li>L.E.D VIDEO WALLS</li>
      <li>AUDIO SOLUTIONS</li>
    </ul>
    <div class="contact-panel">
      <div class="contact-panel__backdrop" role="img" aria-label="Blue geometric backdrop behind contact details"></div>
      <div class="phone">1300 555 019</div>
      <div class="tagline"><span>DESIGN</span><span>–</span><span>CONSULTING</span><span>–</span><span>SERVICE</span><span>–</span><span>MAINTENANCE</span></div>
      <div class="website">www.brightlinkav.com.au</div>
    </div>
  </section>
</body>
</html>
```